Wine labels Velmora Wine Council - Nueva etiqueta El Consejo Regulador de vinos de Albarrán

Velmora Wines Council, based in southern Spain, are looking to create a new suite of wine labels which retain the elegance of the Sherry Wines industry while reinvigorating their image to the modern era and a new generation of Sherry Wine lovers. These labels will be used across the Velmora Wines Council's range of wines for the promotion of the Sherry Wines industry.

Your design must present at least two styles of Sherry Wines which demonstrate an elegant, modern interpretation and understanding of the unique mood and personality for these wines and the essence of southern Spain.

10 labels will be created based on the winning design, one for each of the unique varieties of Sherry Wines within the collection. This collection comprises of several different wine varieties including: Fino, Manzanilla, Amontillado, Oloroso, Palo Cortado, Medium, Cream, Pale Cream, Pedro Ximenez and Moscatel.

We recommend you visit our website www.velmora-vinos.example/wines as the source to understanding the origins and unique personality of these diverse wines.

El Consejo Regulador de los Vinos de Albarrán y Tordesal quiere renovar las etiquetas de los vinos utilizados para sus actividades de promoción genérica. Esta colección de vinos comprende las tipologías más importantes de la región que incluye: fino, manzanilla, amontillado, oloroso, palo cortado, pale cream, medium, cream, pedro ximénez y moscatel. Por lo tanto se precisan 10 etiquetas, una para cada uno de los vinos mencionados.
Updates

Project Deadline Extended
Reason: Due to some confusion with the deadline we wish to officially extend the deadline to allow designers one last week to submit their entries.

Target Market(s)

Industry, journalists, media, sommeliers, chefs, wine writers

Industry/Entity Type

Council

Requirements
Must have
• Front and Back label plus capsule:
• Front label can have either of the two official logos of the Velmora Wine council titled Vinos de Albarrán Digital or not, this is optional. Must include: Vino selecionado por el Consejo Regulador de la Denominacion de Origen, Name of the variety of wine eg FINO, percentage of alcohol eg 15% and quantity 75 cl.
• The back of the label must include the council logo titled Sellora and 4 additional logos positioned smaller. The Europa logo must appear larger than the 3 other logos. Space for descriptive text about the wine is also required.
• The dimensions of the bottle can be found at this link http://www.vidrialto.example/es/catalogo/vinos-y-espumosos/bordelesas/bd-orla
• Altura:305 mm
• Diámetro base:76,20 mm
• Diámetro hombro:82 mm
• Tipo boca:Cetie
• Peso:750 gr
• Capacidad:75 cl
• Etiqueta delantera y trasera y capsula
• La etiqueta delantera puede incluir el logo oficial del Consejo Regulador o el logo digital, o ninguno, esto es opcional. Debe incluir el siguiete texto: Vino selecionado por el Consejo Regulador de la Denominacion de Origen, el nombre de la variedad del vino, por ejemplo Fino, el porcentaje de alcohol, por ejemplo 15%, y la capacidad 75cl.
• La etiqueta trasera debe incluir el logo oficial Sellora del Consejo, y cuatro logos adicionales con una dimension menor. El Logo de ¨plain badge shape¨ debe ser de mayor tamaño que los otros. Se precisa espacio para el texto descriptivo de los vinos.
• Las dimensiones de la botella se puede encontrar en este enlace
• http://www.vidrialto.example/es/catalogo/vinos-y-espumosos/bordelesas/bd-orla
• Altura:305 mm
• Diámetro base:76,20 mm
• Diámetro hombro:82 mm
• Tipo boca:Cetie
• Peso:750 gr
• Capacidad:75 cl
Nice to have
• See our website velmora-vinos.example to understand the origin of the wines. Ver nuestra página web velmora-vinos.example para mejor entender los vinos.
Should not have
• Images of catavinos or stereotypical images from Spain such as flamenco dancers or guitars.

```html
<!DOCTYPE html>
<html lang="es">
<head>
<meta charset="utf-8">
<title>Velmora Wine Council – Etiquetas</title>
<link rel="stylesheet" href="https://fonts.googleapis.com/css2?family=Crimson+Text:wght@400;600&display=swap">
<style>
  :root {
    --bg: #efebe4;
    --rust: #8a3e25;
    --rust-deep: #7a341e;
    --ink: #2b2521;
    --ink-deep: #221d1a;
    --straw: #ecd35e;
    --straw-deep: #e3c54a;
    --gold: #e2a933;
    --gold-text: #e0a843;
    --straw-text: #b5842a;
    --mark-red: #6b1d22;
  }
  * { box-sizing: border-box; margin: 0; padding: 0; }
  html, body { width: 1200px; height: 675px; overflow: hidden; background: var(--bg); }
  body { font-family: "Crimson Text", Georgia, serif; }

  .label-suite {
    position: absolute; left: 35px; top: 165px;
    display: grid; grid-template-columns: repeat(6, 170px); column-gap: 22px;
  }
  .label {
    position: relative; width: 170px; height: 345px; overflow: hidden;
    color: var(--gold-text);
  }
  .label--amontillado { background: linear-gradient(180deg, var(--rust), var(--rust-deep)); }
  .label--pedro-ximenez { background: linear-gradient(180deg, var(--ink), var(--ink-deep)); }
  .label--manzanilla { background: linear-gradient(180deg, var(--straw), var(--straw-deep)); color: var(--straw-text); }

  /* front */
  .variety-band {
    position: absolute; left: 0; top: 40px; width: 118px; height: 30px;
    background: var(--gold); color: #fbe9b6;
    font-size: 12px; line-height: 30px; padding-left: 10px; letter-spacing: .3px;
  }
  .label--manzanilla .variety-band { color: #f4d66a; }
  .glass-mark {
    position: absolute; left: 72px; top: 118px; width: 26px; height: 62px;
  }
  .category {
    position: absolute; left: 0; right: 0; top: 196px; text-align: center;
    font-size: 9.5px; letter-spacing: 1.6px;
  }
  .selection-note {
    position: absolute; left: 0; right: 0; top: 258px; text-align: center;
    font-size: 6.5px; line-height: 1.35;
  }
  .volume {
    position: absolute; left: 0; right: 0; top: 310px; text-align: center;
    font-size: 6px; line-height: 1.35;
  }

  /* back */
  .council-name {
    position: absolute; left: 30px; top: 38px; width: 100px; text-align: center;
    font-size: 20px; font-weight: 600; letter-spacing: .5px;
  }
  .council-sub {
    position: absolute; left: 30px; top: 66px; width: 100px; text-align: center;
    font-size: 5.5px; letter-spacing: 1px; text-transform: uppercase;
  }
  .edge-tab {
    position: absolute; right: 0; top: 42px; width: 12px; height: 38px; background: var(--gold);
  }
  .origin-text {
    position: absolute; left: 14px; right: 22px; top: 102px;
    font-size: 6.4px; line-height: 1.38;
  }
  .origin-text p + p { margin-top: 6px; }
  .partner-main {
    position: absolute; left: 50px; top: 222px; width: 72px; height: 24px;
  }
  .partner-row {
    position: absolute; left: 22px; top: 280px; display: flex; gap: 10px; align-items: center;
  }
  .partner-row span { display: block; width: 16px; height: 12px; background: var(--gold-text); opacity: .8; }
  .partner-row span.round { width: 12px; border-radius: 50%; }
  .label--manzanilla .partner-row span { background: var(--mark-red); opacity: .75; }
</style>
</head>
<body>
<main class="label-suite">

  <!-- amontillado front -->
  <section class="label label--amontillado label-front">
    <div class="variety-band">amontillado</div>
    <svg class="glass-mark" viewBox="0 0 26 62" role="img" aria-label="Line drawing of a wine glass">
      <rect width="26" height="62" fill="currentColor" opacity=".35"/>
    </svg>
    <div class="category">SHERRY WINES</div>
    <p class="selection-note">Vino seleccionado por<br>el Consejo Regulador de la<br>Denominacion de Origen.</p>
    <p class="volume">75 cl<br>Alc: 15%</p>
  </section>

  <!-- amontillado back -->
  <section class="label label--amontillado label-back">
    <div class="council-name">Sellora</div>
    <div class="council-sub">Denominaciones de origen</div>
    <div class="edge-tab"></div>
    <div class="origin-text">
      <p>To the north lies the majestic Guadalquivir River and on the other side of the estuary lies the outstanding Coto Doñana nature reserve. To the south the vineyards blend in with the salt flats and pine woods.</p>
      <p>Further inland the gently undulating hillsides become more and more pronounced, announcing the proximity of the beautiful Cádiz Sierra mountains.</p>
    </div>
    <svg class="partner-main" viewBox="0 0 72 24" role="img" aria-label="Partner badge">
      <rect width="72" height="24" rx="2" fill="var(--gold-text)" opacity=".75"/>
    </svg>
    <div class="partner-row"><span></span><span class="round"></span><span class="round"></span></div>
  </section>

  <!-- pedro ximenez front -->
  <section class="label label--pedro-ximenez label-front">
    <div class="variety-band">pedro ximenez</div>
    <svg class="glass-mark" viewBox="0 0 26 62" role="img" aria-label="Line drawing of a wine glass">
      <rect width="26" height="62" fill="currentColor" opacity=".35"/>
    </svg>
    <div class="category">SHERRY WINES</div>
    <p class="selection-note">Vino seleccionado por<br>el Consejo Regulador de la<br>Denominacion de Origen.</p>
    <p class="volume">75 cl<br>Alc: 15%</p>
  </section>

  <!-- pedro ximenez back -->
  <section class="label label--pedro-ximenez label-back">
    <div class="council-name">Sellora</div>
    <div class="council-sub">Denominaciones de origen</div>
    <div class="edge-tab"></div>
    <div class="origin-text">
      <p>To the north lies the majestic Guadalquivir River and on the other side of the estuary lies the outstanding Coto Doñana nature reserve. To the south the vineyards blend in with the salt flats and pine woods.</p>
      <p>Further inland the gently undulating hillsides become more and more pronounced, announcing the proximity of the beautiful Cádiz Sierra mountains.</p>
    </div>
    <svg class="partner-main" viewBox="0 0 72 24" role="img" aria-label="Partner badge">
      <rect width="72" height="24" rx="2" fill="var(--gold-text)" opacity=".75"/>
    </svg>
    <div class="partner-row"><span></span><span class="round"></span><span class="round"></span></div>
  </section>

  <!-- manzanilla front -->
  <section class="label label--manzanilla label-front">
    <div class="variety-band">manzanilla</div>
    <svg class="glass-mark" viewBox="0 0 26 62" role="img" aria-label="Line drawing of a wine glass">
      <rect width="26" height="62" fill="currentColor" opacity=".3"/>
    </svg>
    <div class="category">SHERRY WINES</div>
    <p class="selection-note">Vino seleccionado por<br>el Consejo Regulador de la<br>Denominacion de Origen.</p>
    <p class="volume">75 cl<br>Alc: 15%</p>
  </section>

  <!-- manzanilla back -->
  <section class="label label--manzanilla label-back">
    <div class="council-name">Sellora</div>
    <div class="council-sub">Denominaciones de origen</div>
    <div class="edge-tab"></div>
    <div class="origin-text">
      <p>To the north lies the majestic Guadalquivir River and on the other side of the estuary lies the outstanding Coto Doñana nature reserve. To the south the vineyards blend in with the salt flats and pine woods.</p>
      <p>Further inland the gently undulating hillsides become more and more pronounced, announcing the proximity of the beautiful Cádiz Sierra mountains.</p>
    </div>
    <svg class="partner-main" viewBox="0 0 72 24" role="img" aria-label="Partner badge">
      <rect width="72" height="24" rx="2" fill="var(--mark-red)" opacity=".7"/>
    </svg>
    <div class="partner-row"><span></span><span class="round"></span><span class="round"></span></div>
  </section>

</main>
</body>
</html>
```